Business Card Design

​Silver Harbor Grooves provides personal, friendly service in a fun and high energy environment. We are based in Vermont.

We would like a card that appeals to a wide range of audiences as we do a wide range of events. Please feel free to check out our website silverharborgrooves.com for inspiration.

Target Market(s)

weddings, corporate, birthday parties, colleges

Industry/Entity Type

Business

Contact Information for Business Card

Silver Harbor Grooves
Providing Entertainment For All Occasions
555 218 6093
silverharborgrooves@mailvane.com
silverharborgrooves.com

```html
<!DOCTYPE html>
<html lang="en">
<head>
<meta charset="utf-8">
<title>Silver Harbor Grooves – Business Card</title>
<link href="https://fonts.googleapis.com/css2?family=Arimo:wght@400;700&display=swap" rel="stylesheet">
<style>
  :root {
    --page-bg: #e9e6e1;
    --card-bg: #3b3b3b;
    --panel-light: #4d4d4d;
    --panel-mid: #454545;
    --panel-line: #2c2c2c;
    --brand-green: #6cbf3f;
    --accent-red: #d8262c;
  }
  * { margin: 0; padding: 0; box-sizing: border-box; }
  html, body {
    width: 1200px;
    height: 918px;
    overflow: hidden;
    background: var(--page-bg);
    font-family: "Arimo", Arial, sans-serif;
  }
  .card {
    position: absolute;
    left: 75px;
    top: 159px;
    width: 1050px;
    height: 600px;
    background: var(--card-bg);
    box-shadow: 0 10px 30px rgba(0,0,0,0.25);
  }
  .brand {
    position: absolute;
    left: 140px;
    top: 105px;
    width: 470px;
    height: 230px;
    display: flex;
    align-items: center;
    gap: 26px;
  }
  .brand-mark {
    flex: 0 0 auto;
    width: 120px;
    height: 120px;
    background: var(--accent-red);
  }
  .brand-name {
    color: var(--brand-green);
    font-weight: 700;
    font-size: 52px;
    line-height: 1.05;
    letter-spacing: 1px;
    text-transform: uppercase;
  }
  .contact-panel {
    position: absolute;
    left: 640px;
    top: 235px;
    width: 390px;
    list-style: none;
  }
  .contact-row {
    height: 34px;
    border-bottom: 2px solid var(--panel-line);
    background: var(--panel-mid);
    color: var(--brand-green);
    font-size: 15px;
    line-height: 32px;
    padding-left: 14px;
    white-space: nowrap;
  }
  .contact-row:nth-child(odd) { background: var(--panel-light); }
  .tagline {
    position: absolute;
    left: 160px;
    top: 470px;
    color: var(--accent-red);
    font-weight: 700;
    font-size: 23px;
    white-space: nowrap;
  }
</style>
</head>
<body>
  <div class="card">
    <div class="brand">
      <span class="brand-mark"></span>
      <span class="brand-name">Silver Harbor<br>Grooves</span>
    </div>
    <ul class="contact-panel">
      <li class="contact-row">E-mail: silverharborgrooves@mailvane.com</li>
      <li class="contact-row"></li>
      <li class="contact-row">Tel.: 555 218 6093</li>
      <li class="contact-row"></li>
      <li class="contact-row">silverharborgrooves.com</li>
      <li class="contact-row"></li>
    </ul>
    <p class="tagline">Silver Harbor Grooves Providing Entertainment For All Occasions</p>
  </div>
</body>
</html>
```